We are looking for a graphic design for a trade show banner. The banner will be 10 feet x 10 feet. We are an adventure based tour operator in Costa Rica. The graphic should inspire a sense of adventure as well as being clear and not too cluttered. Our website is www.pumaverdetrips.com

The following text should be used on the banner:

1. Our Logo (attached)
2. 8 Days. 8 Adventures. 1 Life
3. Seven Wild Sunrises (name of the tour we are selling). The "Seven Wild Sunrises" wording should be prominent. Underneath, or somewhere close to that wording there should be, in smaller text, "All inclusive Costa Rica Adventure Tour"
4. Price $1799 with a slash through it and then special promotion price of $1449. Text should read "Book this weekend and save $350!"
5. Terra Vista Journal Logo (Attached)
6. "Rafting, ziplining, kayaking, surfing, snorkeling, wildlife, jungle lodge, waterfall rappelling, hiking, mountain biking"
7. www.PumaVerdeTrips.com

We have attached some pictures. Not all need to be used but the rafting photo definitely needs to be used.

Industry/Entity Type

Graphic Design

Colors
33a6d7
3276b5
0355a3

```html
<!DOCTYPE html>
<html lang="en">
<head>
<meta charset="UTF-8">
<title>Seven Wild Sunrises – Puma Verde Trips</title>
<link rel="stylesheet" href="https://fonts.googleapis.com/css2?family=Fira+Sans:wght@500;700&family=Roboto:wght@900&family=Roboto+Condensed:wght@700&display=swap">
<style>
  :root {
    --blue-deep: #0b56a4;
    --blue-mid: #3276b5;
    --blue-sky: #33a6d7;
    --orange: #f0691c;
    --gold: #f6a31f;
    --ink: #0a0a0a;
    --grey: #9e9e9e;
    --cream: #f3ecdc;
    --white: #ffffff;
    --yellow: #f2c400;
  }
  * { margin: 0; padding: 0; box-sizing: border-box; }
  html, body { width: 1200px; height: 1200px; overflow: hidden; background: var(--white); }
  .banner { position: relative; width: 1200px; height: 1200px; overflow: hidden; background: var(--grey); font-family: "Fira Sans", sans-serif; }

  .left-panel { position: absolute; left: 0; top: 0; width: 646px; height: 1200px; background: var(--blue-deep); }

  .photos { position: absolute; left: 646px; top: 0; width: 554px; height: 1200px; }

  .brand { position: absolute; left: 44px; top: 62px; display: flex; align-items: center; gap: 22px; }
  .brand-name { color: var(--gold); font-family: "Fira Sans", sans-serif; font-weight: 500; font-size: 54px; line-height: 1; }
  .brand-mark { width: 58px; height: 58px; border-radius: 50%; background: var(--blue-sky); }

  .tagline { position: absolute; left: 44px; top: 196px; color: var(--white); font-weight: 500; font-size: 34px; letter-spacing: 0.5px; }

  .tour-title { position: absolute; left: 40px; top: 276px; color: var(--orange); font-family: "Roboto", sans-serif; font-weight: 900; font-size: 96px; line-height: 102px; letter-spacing: -1px; paint-order: stroke fill; -webkit-text-stroke: 3px var(--white); }

  .tour-sub { position: absolute; left: 40px; top: 620px; color: var(--white); font-family: "Roboto Condensed", sans-serif; font-weight: 700; font-size: 29px; }

  .website { position: absolute; left: 40px; top: 698px; color: var(--white); font-weight: 500; font-size: 25px; letter-spacing: 0.3px; }

  .activities { position: absolute; left: 0; top: 770px; width: 658px; height: 148px; background: var(--ink); color: var(--white); font-weight: 500; font-size: 22.5px; line-height: 42px; padding: 14px 20px 0 28px; }

  .award-badge { position: absolute; left: 55px; top: 950px; width: 167px; height: 212px; background: var(--ink); }
  .award-rule { position: absolute; left: 240px; top: 953px; width: 3px; height: 208px; background: var(--yellow); }

  .price-tag { position: absolute; left: 442px; top: 888px; width: 184px; height: 300px; background: var(--cream); box-shadow: 2px 3px 6px rgba(0,0,0,0.35); text-align: center; }
  .price-tag .tag-head { height: 112px; background: var(--blue-sky); color: var(--white); font-family: "Roboto Condensed", sans-serif; font-weight: 700; font-size: 19px; line-height: 24px; padding-top: 52px; }
  .price-tag .tag-hole { position: absolute; left: 80px; top: 14px; width: 24px; height: 24px; border-radius: 50%; background: var(--ink); border: 4px solid #cfcfcf; }
  .price-old { margin-top: 10px; color: var(--orange); font-family: "Roboto Condensed", sans-serif; font-weight: 700; font-size: 30px; text-decoration: line-through; text-decoration-thickness: 3px; }
  .price-new { color: var(--orange); font-family: "Roboto Condensed", sans-serif; font-weight: 700; font-size: 54px; line-height: 1.05; }
  .price-note { color: var(--blue-deep); font-family: "Roboto Condensed", sans-serif; font-weight: 700; font-size: 16px; }
  .price-save { color: var(--blue-deep); font-family: "Roboto Condensed", sans-serif; font-weight: 700; font-size: 27px; line-height: 1.1; }
  .price-bar { width: 34px; height: 5px; border-radius: 3px; background: var(--blue-mid); margin: 4px 0 0 20px; }
</style>
</head>
<body>
<div class="banner">
  <div class="left-panel"></div>

  <svg class="photos" viewBox="0 0 554 1200" width="554" height="1200">
    <defs>
      <linearGradient id="raftTones" x1="0" y1="0" x2="1" y2="1">
        <stop offset="0" stop-color="#3e5a2a"/>
        <stop offset="0.5" stop-color="#8d8f86"/>
        <stop offset="1" stop-color="#d8e2e8"/>
      </linearGradient>
      <linearGradient id="zipTones" x1="0" y1="0" x2="1" y2="1">
        <stop offset="0" stop-color="#5f7a2c"/>
        <stop offset="0.5" stop-color="#7e9a3a"/>
        <stop offset="1" stop-color="#2e4a1e"/>
      </linearGradient>
    </defs>
    <polygon role="img" aria-label="Photo: a team paddling a blue raft through whitewater rapids" points="0,0 400,0 554,90 554,612 0,474" fill="url(#raftTones)"/>
    <polygon role="img" aria-label="Photo: a smiling guest in a red helmet riding a zipline through the jungle" points="0,600 554,712 554,1152 506,1200 0,1200" fill="url(#zipTones)"/>
  </svg>

  <div class="brand">
    <span class="brand-name">Puma Verde Trips</span>
    <span class="brand-mark"></span>
  </div>

  <p class="tagline">8 Days. 8 Adventures. 1 Life</p>

  <h1 class="tour-title">Seven<br>Wild<br>Sunrises</h1>

  <p class="tour-sub">All inclusive Costa Rica Adventure Tour</p>

  <p class="website">www.PumaVerdeTrips.com</p>

  <p class="activities">Rafting, Ziplining, Kayaking, Surfing, Snorkeling,<br>Wildlife, Jungle Lodge, Waterfall Rappelling, Hiking,<br>Mountain Biking</p>

  <div class="award-badge" role="img" aria-label="Terra Vista Journal award badge"></div>
  <div class="award-rule"></div>

  <div class="price-tag">
    <div class="tag-hole"></div>
    <div class="tag-head">SPECIAL PROMOTION<br>PRICE</div>
    <div class="price-old">$1799</div>
    <div class="price-new">$1449</div>
    <div class="price-note">Book this weekend</div>
    <div class="price-save">Save $350</div>
    <div class="price-bar"></div>
  </div>
</div>
</body>
</html>
```